Dentist logo, business card and website

I have done an amateur job of creating a logo, business card and website. I would like it to look more professional. the current website can be found at www.dorenkamsel.com - I would like the website to be built and run through wix.com. The content on the website is as I would like it but I am open to suggestions.

The logo should be simple, may be best to keep to the letter DK - maybe to look like the V is a reflection of the A? Again, I am open to suggestions (I have attached a couple of images I have used on presentations but I would like the logo that you design to have a 'no fill' background so it can be placed on slides (for presentations etc).

The colour scheme seems wrong for a dentist, perhaps duck egg with black writing would be better? This applies to the business card as well (I have attached a PDF of some I have had made in the past but again they look amateur and colour scheme is wrong. The business cards should be landscape, have the logo in the top right corner, my name and qualifications in the middle, and my website and physical address in the bottom left corner: Glanmorfa Dental Surgery, 41-43 Ffordd y Bont, Cardiff CF23 9RT.

Target Market(s)

30-60 year olds

Industry/Entity Type

Dental

Contact Information for Business Card

Please see brief and uploads.

Logo Text

DK

Number of Pages Required

4 page

Font styles to use
Decorative
Script

Requirements
Must have
• A sophisticated mature feel.
Nice to have
• Simplicity.
Should not have
• Anything too complicated.

```html
<!DOCTYPE html>
<html lang="en">
<head>
<meta charset="utf-8">
<title>Doren Kamsel — Restorative &amp; Implant Dentist</title>
<link rel="stylesheet" href="https://fonts.googleapis.com/css2?family=Raleway:wght@400;500;600;700&family=Open+Sans:wght@400;600&display=swap">
<style>
  :root {
    --teal: #2f8a94;
    --teal-dark: #1f5f68;
    --ink: #2b2b2b;
    --muted: #7a7a7a;
    --tan: #b38f5c;
    --tan-dark: #8c6b3e;
    --tan-card: rgba(176, 138, 86, 0.88);
    --duck-egg: #cfe6ec;
    --footer: #bfdde5;
    --paper: #ffffff;
    --light: #f2f2f2;
  }
  * { box-sizing: border-box; margin: 0; padding: 0; }
  html, body { width: 893px; height: 1200px; overflow: hidden; }
  body { font-family: "Open Sans", sans-serif; color: var(--ink); background: var(--paper); position: relative; }

  .topbar { height: 22px; display: flex; justify-content: flex-end; align-items: center; gap: 28px; padding: 0 28px; font-size: 9px; color: var(--muted); background: var(--paper); }
  .topbar span { display: flex; align-items: center; gap: 4px; }

  .masthead { height: 68px; display: flex; align-items: center; justify-content: space-between; padding: 0 24px 0 18px; background: var(--paper); border-bottom: 1px solid #e6e6e6; }
  .brand { display: flex; align-items: center; gap: 8px; }
  .brand-mark { width: 14px; height: 14px; background: var(--teal); border-radius: 50%; }
  .brand-name { font-family: "Raleway", sans-serif; font-weight: 600; font-size: 20px; letter-spacing: 1px; color: var(--teal); }
  .brand-tag { font-size: 7.5px; color: var(--muted); letter-spacing: .5px; margin-top: 1px; }
  .main-nav { display: flex; gap: 34px; font-family: "Raleway", sans-serif; font-size: 11px; font-weight: 600; color: var(--ink); }

  .hero { position: relative; height: 432px; overflow: hidden; }
  .hero-photo { position: absolute; inset: 0; background: radial-gradient(ellipse at 70% 40%, #d8d9db 0%, #a9abae 45%, #6d7073 100%); }
  .hero-copy { position: absolute; top: 150px; left: 0; right: 0; text-align: center; color: #fff; }
  .hero-title { font-family: "Raleway", sans-serif; font-weight: 600; font-size: 26px; letter-spacing: 1px; line-height: 1.2; }
  .hero-sub { font-size: 13px; margin-top: 4px; }
  .hero-dots { position: absolute; right: 14px; top: 160px; display: flex; flex-direction: column; gap: 6px; }
  .hero-dots i { width: 5px; height: 5px; background: #fff; border-radius: 50%; display: block; }
  .services { position: absolute; top: 244px; left: 48px; right: 48px; display: flex; justify-content: space-between; }
  .service-card { width: 238px; height: 134px; background: var(--tan-card); color: #fff; padding: 14px 14px; }
  .service-card h3 { font-family: "Raleway", sans-serif; font-size: 12px; font-weight: 600; letter-spacing: .5px; margin-bottom: 8px; }
  .service-card p { font-size: 8.5px; line-height: 1.5; margin-bottom: 12px; }
  .read-more { display: inline-block; background: var(--tan-dark); font-size: 8.5px; padding: 5px 11px; }

  .appointment { height: 58px; background: var(--duck-egg); display: flex; align-items: center; padding-left: 150px; gap: 92px; }
  .appointment h2 { font-family: "Raleway", sans-serif; font-weight: 500; font-size: 17px; color: var(--teal-dark); letter-spacing: .5px; }
  .btn { background: var(--tan); color: #fff; font-size: 11px; padding: 9px 22px; }

  .care { height: 432px; text-align: center; padding-top: 150px; }
  .section-title { font-family: "Raleway", sans-serif; font-weight: 500; font-size: 20px; letter-spacing: .5px; color: var(--ink); }
  .rule { width: 90px; height: 1px; background: #ccc; margin: 12px auto 0; }
  .features { display: flex; justify-content: center; gap: 64px; margin-top: 36px; }
  .feature { width: 190px; }
  .feature-icon { width: 56px; height: 56px; border-radius: 50%; background: var(--tan); margin: 0 auto 16px; display: flex; align-items: center; justify-content: center; }
  .feature h4 { font-family: "Raleway", sans-serif; font-size: 12px; font-weight: 600; letter-spacing: .3px; margin-bottom: 8px; }
  .feature p { font-size: 8.5px; color: var(--muted); line-height: 1.5; }

  .newsletter { height: 104px; background: var(--light); text-align: center; padding-top: 30px; }
  .newsletter .section-title { font-size: 18px; line-height: 1.2; }
  .newsletter-sub { font-size: 9.5px; color: var(--muted); margin-top: 4px; }
  .signup { display: flex; justify-content: center; gap: 8px; margin-top: 10px; }
  .signup-field { width: 552px; height: 22px; border: 1px solid #d2d2d2; background: #fff; font-size: 8.5px; color: var(--muted); text-align: left; padding: 5px 8px; }
  .signup-btn { width: 96px; height: 22px; background: var(--tan); color: #fff; font-size: 8.5px; padding-top: 5px; }

  .footer { height: 94px; background: var(--footer); padding: 30px 40px 0; display: flex; justify-content: space-between; font-size: 9px; color: var(--ink); }
  .footer-info p { margin-bottom: 12px; }
  .footer-contact { display: flex; gap: 30px; }
  .footer-contact span { display: flex; align-items: center; gap: 4px; }
  .social { display: flex; gap: 6px; margin-top: 2px; }
  .social i { width: 14px; height: 14px; background: var(--teal-dark); display: block; }
</style>
</head>
<body>
  <div class="topbar">
    <span><svg width="8" height="10" viewBox="0 0 8 10"><path d="M4 0a4 4 0 0 0-4 4c0 3 4 6 4 6s4-3 4-6a4 4 0 0 0-4-4z" fill="#2f8a94"/><circle cx="4" cy="4" r="1.4" fill="#fff"/></svg>Glanmorfa Dental Surgery, 41-43 Ffordd y Bont, Cardiff CF23 9RT</span>
    <span><svg width="9" height="9" viewBox="0 0 10 10"><path d="M2 0l2 2.5-1.2 1.3a6 6 0 0 0 3.4 3.4L7.5 6 10 8l-1.5 2C4 10 0 6 0 1.5z" fill="#2f8a94"/></svg>029 2049 7316</span>
  </div>

  <header class="masthead">
    <div class="brand">
      <div class="brand-mark"></div>
      <div>
        <div class="brand-name">DOREN KAMSEL</div>
        <div class="brand-tag">Restorative &amp; Implant Dentistry</div>
      </div>
    </div>
    <nav class="main-nav">
      <span>HOME</span><span>ABOUT ME</span><span>TESTIMONIALS</span><span>PATIENT RESOURCES</span><span>CONTACT</span>
    </nav>
  </header>

  <section class="hero">
    <div class="hero-photo" role="img" aria-label="Soft grey photograph of a dental instrument beside a model tooth"></div>
    <div class="hero-copy">
      <h1 class="hero-title">WELCOME TO DOREN KAMSEL</h1>
      <p class="hero-sub">I am a restorative and implant dentist based in Cardiff</p>
    </div>
    <div class="hero-dots"><i></i><i></i><i></i></div>
    <div class="services">
      <article class="service-card">
        <h3>PROFESSIONAL EXPERIENCE</h3>
        <p>Thoughtful restorative care built around comfort, clear advice and results that last.</p>
        <span class="read-more">Read More</span>
      </article>
      <article class="service-card">
        <h3>DENTAL IMPLANTOLOGY</h3>
        <p>Thoughtful restorative care built around comfort, clear advice and results that last.</p>
        <span class="read-more">Read More</span>
      </article>
      <article class="service-card">
        <h3>SAME-DAY CROWNS</h3>
        <p>Thoughtful restorative care built around comfort, clear advice and results that last.</p>
        <span class="read-more">Read More</span>
      </article>
    </div>
  </section>

  <section class="appointment">
    <h2>SCHEDULE YOUR APPOINTMENT ONLINE</h2>
    <span class="btn">Book an Appointment</span>
  </section>

  <section class="care">
    <h2 class="section-title">TAKING CARE OF YOUR HEALTH</h2>
    <div class="rule"></div>
    <div class="features">
      <div class="feature">
        <div class="feature-icon"><svg width="24" height="24" viewBox="0 0 24 24"><rect x="4" y="3" width="16" height="19" rx="2" fill="none" stroke="#fff" stroke-width="2"/><path d="M8 12l3 3 5-6" fill="none" stroke="#fff" stroke-width="2"/></svg></div>
        <h4>HEALTH PLANS WE ACCEPT</h4>
        <p>Friendly, careful treatment planned with you and explained every step of the way.</p>
      </div>
      <div class="feature">
        <div class="feature-icon"><svg width="22" height="26" viewBox="0 0 22 26"><path d="M11 1a9 9 0 0 0-9 9c0 7 9 15 9 15s9-8 9-15a9 9 0 0 0-9-9z" fill="#fff"/><circle cx="11" cy="10" r="3.5" fill="#b38f5c"/></svg></div>
        <h4>CLINIC IN THE AREA</h4>
        <p>Friendly, careful treatment planned with you and explained every step of the way.</p>
      </div>
      <div class="feature">
        <div class="feature-icon"><svg width="24" height="24" viewBox="0 0 24 24"><path d="M9 3h6v6h6v6h-6v6H9v-6H3V9h6z" fill="#fff"/></svg></div>
        <h4>SPECIALIST DOCTORS</h4>
        <p>Friendly, careful treatment planned with you and explained every step of the way.</p>
      </div>
    </div>
  </section>

  <section class="newsletter">
    <h2 class="section-title">SIGN UP FOR OUR NEWSLETTER</h2>
    <p class="newsletter-sub">Join the mailing list for practice news, tips and updates from the surgery.</p>
    <div class="signup">
      <div class="signup-field">Email Address</div>
      <div class="signup-btn">Subscribe Now</div>
    </div>
  </section>

  <footer class="footer">
    <div class="footer-info">
      <p>Copyright © 2017 by Doren Kamsel . All Rights Reserved</p>
      <div class="footer-contact">
        <span><svg width="8" height="10" viewBox="0 0 8 10"><path d="M4 0a4 4 0 0 0-4 4c0 3 4 6 4 6s4-3 4-6a4 4 0 0 0-4-4z" fill="#1f5f68"/><circle cx="4" cy="4" r="1.4" fill="#bfdde5"/></svg>Glanmorfa Dental Surgery, 41-43 Ffordd y Bont, Cardiff CF23 9RT</span>
        <span><svg width="9" height="9" viewBox="0 0 10 10"><path d="M2 0l2 2.5-1.2 1.3a6 6 0 0 0 3.4 3.4L7.5 6 10 8l-1.5 2C4 10 0 6 0 1.5z" fill="#1f5f68"/></svg>029 2049 7316</span>
      </div>
    </div>
    <div class="social"><i></i><i></i><i></i><i></i></div>
  </footer>
</body>
</html>
```